Tallowcrest Rise A4 Potrait foldout brochure

We need a brochure design for this residential land development. I have attached the a style that we like to base our design on. Full colour required. will provide files required for design also. PLEASE DO NOT COPY THIS DESIGN. Come up with a new style that gives you this feeling. Please note the plan needs to be positioned landscape on the inside 2 A4 Pages.

Industry/Entity Type

Residential

Other font styles liked:
• Try with Century Gothich

Requirements
Must have
• use same colours as supplied in Tallowcrest rise brochure.
Nice to have
• nice modern simple background graphics

```html
<!DOCTYPE html>
<html lang="en">
<head>
<meta charset="utf-8">
<title>Tallowcrest Rise – Presentation Folder</title>
<link href="https://fonts.googleapis.com/css2?family=Lato:wght@400;700&display=swap" rel="stylesheet">
<style>
  :root {
    --page-bg: #e4e5e6;
    --paper: #fbfbfa;
    --ink-green: #0a5428;
    --white: #ffffff;
    --orange: #f59a45;
    --amber: #f8bd4f;
    --violet: #a97cc6;
    --rose: #d6a0c4;
    --leaf: #4fae5c;
    --slate: #7d8c92;
    --lime: #a8c65a;
  }
  * { box-sizing: border-box; margin: 0; padding: 0; }
  html, body { width: 1200px; height: 867px; overflow: hidden; }
  body { background: var(--page-bg); font-family: "Lato", Arial, sans-serif; position: relative; }

  .folder {
    position: absolute; left: 40px; top: 38px; width: 1120px; height: 791px;
    background: var(--paper);
    box-shadow: 0 2px 10px rgba(0,0,0,0.18);
    overflow: hidden;
  }
  .folder__colour-field {
    position: absolute; inset: 0;
    clip-path: polygon(0 343px, 560px 449px, 1120px 343px, 1120px 791px, 0 791px);
    background:
      radial-gradient(ellipse 240px 260px at 120px 560px, var(--orange) 0%, rgba(245,154,69,0) 100%),
      radial-gradient(ellipse 200px 200px at 140px 420px, var(--amber) 0%, rgba(248,189,79,0) 100%),
      radial-gradient(ellipse 220px 260px at 400px 640px, var(--violet) 0%, rgba(169,124,198,0) 100%),
      radial-gradient(ellipse 180px 200px at 310px 580px, var(--rose) 0%, rgba(214,160,196,0) 100%),
      radial-gradient(ellipse 200px 300px at 600px 560px, var(--leaf) 0%, rgba(79,174,92,0) 100%),
      radial-gradient(ellipse 220px 240px at 820px 520px, var(--violet) 0%, rgba(169,124,198,0) 100%),
      radial-gradient(ellipse 200px 220px at 1010px 700px, var(--orange) 0%, rgba(245,154,69,0) 100%),
      radial-gradient(ellipse 200px 200px at 1080px 420px, var(--lime) 0%, rgba(168,198,90,0) 100%),
      radial-gradient(ellipse 200px 200px at 930px 400px, var(--amber) 0%, rgba(248,189,79,0) 100%),
      linear-gradient(90deg, var(--orange), var(--slate) 40%, var(--leaf) 55%, var(--violet) 75%, var(--lime));
  }
  .folder__edge-line { position: absolute; inset: 0; pointer-events: none; }
  .folder__fold {
    position: absolute; left: 559px; top: 0; width: 2px; height: 100%;
    background: linear-gradient(90deg, rgba(0,0,0,0.05), rgba(255,255,255,0.25));
  }

  .contact-card {
    position: absolute; left: 129px; top: 204px; width: 300px; height: 353px;
    background: var(--white);
    box-shadow: 0 1px 5px rgba(0,0,0,0.25);
    text-align: center; color: var(--ink-green);
  }
  .contact-card__name {
    position: absolute; left: 0; right: 0; top: 138px;
    font-size: 31px; font-weight: 400; letter-spacing: -0.2px;
  }
  .contact-card__details { position: absolute; left: 0; right: 0; top: 202px; font-size: 14px; line-height: 19px; }
  .contact-card__address { margin-bottom: 7px; }
  .contact-card__phone { font-size: 18px; font-weight: 700; margin-bottom: 6px; }
  .contact-card__line { margin-bottom: 4px; }
  .icon { display: inline-block; vertical-align: -1px; margin-right: 4px; fill: var(--ink-green); }

  .cover-title {
    position: absolute; left: 560px; width: 560px; top: 238px;
    text-align: center; color: var(--ink-green);
  }
  .cover-title__name { font-size: 49px; font-weight: 400; letter-spacing: -0.3px; line-height: 1; }
  .cover-title__locality {
    position: absolute; right: 69px; top: 54px;
    font-size: 12px; font-weight: 400;
  }
  .cover-web {
    position: absolute; left: 560px; width: 560px; top: 724px;
    text-align: center; color: var(--white);
    font-size: 21px; font-weight: 700;
    text-shadow: 0 1px 3px rgba(0,0,0,0.45);
  }
</style>
</head>
<body>
  <main class="folder">
    <div class="folder__colour-field" role="img" aria-label="Soft multicolour background of orange, violet, green and lime with a faint lattice pattern"></div>
    <svg class="folder__edge-line" width="1120" height="791" viewBox="0 0 1120 791" aria-hidden="true">
      <polyline points="0,352 560,458 1120,352" fill="none" stroke="#ffffff" stroke-width="2.5"/>
    </svg>
    <div class="folder__fold"></div>

    <section class="contact-card">
      <h2 class="contact-card__name">Tallowcrest Rise</h2>
      <div class="contact-card__details">
        <p class="contact-card__address">
          <svg class="icon" width="10" height="13" viewBox="0 0 10 13"><path d="M5 0a5 5 0 0 0-5 5c0 3.5 5 8 5 8s5-4.5 5-8a5 5 0 0 0-5-5zm0 7a2 2 0 1 1 0-4 2 2 0 0 1 0 4z"/></svg>Tallowcrest Rise<br>
          Marrowind Lane 48b<br>
          20817 City, State
        </p>
        <p class="contact-card__phone">
          <svg class="icon" width="16" height="16" viewBox="0 0 16 16"><circle cx="8" cy="8" r="7" fill="none" stroke="#0a5428" stroke-width="1.4"/><path d="M5.6 4.2l1.3 1.6-.8 1c.5 1 1.2 1.8 2.2 2.3l1-.8 1.6 1.3-.9 1.4c-2.5-.4-4.7-2.6-5.1-5.1z"/></svg>+01 23 4560187
        </p>
        <p class="contact-card__line">
          <svg class="icon" width="15" height="11" viewBox="0 0 15 11"><rect width="15" height="11" rx="1"/><path d="M1 1.5l6.5 4.5 6.5-4.5" fill="none" stroke="#fff" stroke-width="1.2"/></svg>info@tallowcrestrise.com
        </p>
        <p class="contact-card__line">
          <svg class="icon" width="14" height="14" viewBox="0 0 14 14" fill="none" stroke="#0a5428" stroke-width="1.2"><circle cx="7" cy="7" r="6"/><ellipse cx="7" cy="7" rx="2.6" ry="6"/><path d="M1 7h12M2 3.8h10M2 10.2h10"/></svg>www.tallowcrestrise.com
        </p>
      </div>
    </section>

    <header class="cover-title">
      <h1 class="cover-title__name">Tallowcrest Rise</h1>
      <p class="cover-title__locality">Wattlegrove Park</p>
    </header>

    <p class="cover-web">www.tallowcrestrise.com</p>
  </main>
</body>
</html>
```